Velvet Leaf needs a luxury packaging design

I'm starting a tea brand from the ground up. The working name as of now is Velvet Leaf. I intend for it to be a luxury loose leaf tea brand.

I want the aesthetic of it to be luxurious in nature. The color schemes that I am liking right now include black, gold, silver, rose gold and anything along that luxury feel line. One of the things I love most is UNIQUE packaging of the tea itself. I'll attach inspiration below.

I want the consumer every single time they use this product to feel like it is an experience. The person I choose will also be the person I consider for all further needs on a design basis moving forward if they would like to continue to work with me.

This is a really great opportunity to work with a luxury line that also does social good as some proceeds from each purchase will go to a mental health awareness cause.

The key is for the packaging to represent luxury, give off a unique feel that gets the consumer excited to see it and show it off to their peers on social media

Target Market(s)

The Modern Millenial, 21-40 (bullseye 28). He or she is a young professional that has a disposable income in which they do like to indulge with. They balance their demanding work schedules well and they have a work hard/play hard mindset. This professional is more likely to order their daily coffee from Brewlane as opposed to Rob Kessler and their social media profiles are a big indicator as to their hobbies and lifestyles outside of their work environment. They enjoy shopping at stores like Vexo, Halvard, Quillway/Quillmen and for special occasions are willing to splurge at stores like Orsolo's, Maison Derel and… They live a pretty active lifestyle and are highly influenced by social media trending products

Requirements
Must have
• Luxurious, must have exclusive look
Nice to have
• unique packaging
• viral inspired design
Should not have
• brown color, childish feel, bubble letters

```html
<!DOCTYPE html>
<html lang="en">
<head>
<meta charset="utf-8">
<title>Velvet Leaf — Tea Box Dieline</title>
<link rel="stylesheet" href="https://fonts.googleapis.com/css2?family=Montserrat:wght@500&family=Oswald:wght@600&family=Cormorant+Garamond:wght@500&display=swap">
<style>
  :root {
    --paper: #ffffff;
    --flap: #0b0b0b;
    --band-dark: #0e0e0e;
    --band-mid: #1c1c1c;
    --band-light: #262626;
    --wood-dark: #121212;
    --wood-light: #3a3a3a;
    --fold-line: #d9d9d9;
    --silver: #bdbdbd;
    --silver-soft: #9a9a9a;
    --tagline: #2b2b2b;
  }
  html, body {
    margin: 0;
    padding: 0;
    width: 1200px;
    height: 731px;
    overflow: hidden;
    background: var(--paper);
  }
  .dieline {
    display: block;
    width: 1200px;
    height: 731px;
  }
  .flap { fill: var(--flap); stroke: var(--flap); stroke-width: 10; stroke-linejoin: round; }
  .fold { fill: none; stroke: var(--fold-line); stroke-width: 0.8; stroke-dasharray: 1.5 2.5; }
  .slot { fill: none; stroke: var(--fold-line); stroke-width: 0.9; stroke-dasharray: 1.5 2; }
  .brand-rule { stroke: var(--silver-soft); stroke-width: 1; }
  .brand-name {
    font-family: "Cormorant Garamond", serif;
    font-weight: 500;
    font-size: 30px;
    letter-spacing: 2px;
    fill: var(--silver);
    text-anchor: middle;
  }
  .tagline {
    font-family: "Oswald", sans-serif;
    font-weight: 600;
    font-size: 16px;
    letter-spacing: 1.5px;
    fill: var(--tagline);
    text-anchor: middle;
  }
</style>
</head>
<body>
<svg class="dieline" viewBox="0 0 1200 731" xmlns="http://www.w3.org/2000/svg">
  <defs>
    <linearGradient id="band-left" x1="0" x2="1" y1="0" y2="0">
      <stop offset="0" stop-color="#1e1e1e"/>
      <stop offset="1" stop-color="#141414"/>
    </linearGradient>
    <linearGradient id="band-right" x1="0" x2="1" y1="0" y2="0">
      <stop offset="0" stop-color="#141414"/>
      <stop offset="1" stop-color="#1f1f1f"/>
    </linearGradient>
    <linearGradient id="band-edge-left" x1="0" x2="1">
      <stop offset="0" stop-color="#161616"/>
      <stop offset="1" stop-color="#080808"/>
    </linearGradient>
    <linearGradient id="band-edge-right" x1="0" x2="1">
      <stop offset="0" stop-color="#080808"/>
      <stop offset="1" stop-color="#161616"/>
    </linearGradient>
    <radialGradient id="wood" cx="0.5" cy="0.55" r="0.6">
      <stop offset="0" stop-color="var(--wood-light)"/>
      <stop offset="1" stop-color="var(--wood-dark)"/>
    </radialGradient>
    <linearGradient id="triangle-top" x1="0" x2="0" y1="0" y2="1">
      <stop offset="0" stop-color="#2a2a2a"/>
      <stop offset="0.75" stop-color="#1f1f1f"/>
      <stop offset="1" stop-color="#0d0d0d"/>
    </linearGradient>
    <linearGradient id="triangle-bottom" x1="0" x2="0" y1="1" y2="0">
      <stop offset="0" stop-color="#2a2a2a"/>
      <stop offset="0.75" stop-color="#1f1f1f"/>
      <stop offset="1" stop-color="#0d0d0d"/>
    </linearGradient>
  </defs>

  <!-- Side band -->
  <g class="band">
    <rect x="71" y="287" width="271" height="151" fill="url(#band-left)" role="img" aria-label="Fine geometric line pattern in dark grey"/>
    <rect x="340" y="287" width="58" height="151" fill="url(#band-edge-left)"/>
    <rect x="398" y="287" width="324" height="151" fill="url(#wood)" role="img" aria-label="Dark charcoal wood plank texture"/>
    <rect x="722" y="287" width="58" height="151" fill="url(#band-edge-right)"/>
    <rect x="780" y="287" width="353" height="151" fill="url(#band-right)" role="img" aria-label="Fine geometric line pattern in dark grey"/>
    <line class="fold" x1="1044" y1="287" x2="1044" y2="438"/>
    <path class="slot" d="M974 326 L990 334 L1006 326 L1012 326 L1012 398 L974 398 L985 382 L990 362 L985 346 Z"/>
    <path class="slot" d="M1066 326 L1104 326 L1100 398 L1070 398 Z"/>
  </g>

  <!-- Top end flaps -->
  <g class="end-top">
    <polygon class="flap" points="330,232 478,26 558,80 398,284"/>
    <polygon class="flap" points="642,26 790,232 722,284 562,80"/>
    <polygon points="560,78 722,286 398,286" fill="url(#triangle-top)" role="img" aria-label="Fine geometric line pattern in dark grey"/>
    <polyline class="fold" points="398,286 560,78 722,286"/>
    <line class="fold" x1="398" y1="287" x2="722" y2="287"/>
    <line class="brand-rule" x1="512" y1="149" x2="530" y2="149"/>
    <line class="brand-rule" x1="590" y1="149" x2="608" y2="149"/>
    <text class="brand-name" x="560" y="159" style="font-size:15px;letter-spacing:1.5px">VELVET</text>
    <text class="brand-name" x="560" y="200">LEAF</text>
    <text class="tagline" x="560" y="258">PREMIUM LEAF TEA</text>
  </g>

  <!-- Bottom end flaps -->
  <g class="end-bottom" transform="rotate(180 560 362.5)">
    <polygon class="flap" points="330,232 478,26 558,80 398,284"/>
    <polygon class="flap" points="642,26 790,232 722,284 562,80"/>
    <polygon points="560,78 722,286 398,286" fill="url(#triangle-top)" role="img" aria-label="Fine geometric line pattern in dark grey"/>
    <polyline class="fold" points="398,286 560,78 722,286"/>
    <line class="fold" x1="398" y1="287" x2="722" y2="287"/>
    <line class="brand-rule" x1="512" y1="149" x2="530" y2="149"/>
    <line class="brand-rule" x1="590" y1="149" x2="608" y2="149"/>
    <text class="brand-name" x="560" y="159" style="font-size:15px;letter-spacing:1.5px">VELVET</text>
    <text class="brand-name" x="560" y="200">LEAF</text>
    <text class="tagline" x="560" y="258">PREMIUM LEAF TEA</text>
  </g>
</svg>
</body>
</html>
```